Website design for commercial and residential security company

we're looking to see some new designs for an established company with no website.

homepage and one inner page

here is a link to the homepage content, sitemap, logo and more.
https://files.brontavel.net/share/7QxmPzLrTw2vNkdJhYcsa9eFgbUoiVwRn?view=open

call to action should be Request A Quote

if you have any questions please send them to us asap

thank you

1 page

Sans Serif

```html
<!DOCTYPE html>
<html lang="en">
<head>
<meta charset="utf-8">
<title>Harborline Business Solutions – Home</title>
<link href="https://fonts.googleapis.com/css2?family=Montserrat:wght@400;500;600;700&display=swap" rel="stylesheet">
<style>
:root{
  --teal:#0b6b73;
  --teal-deep:#0a5f67;
  --orange:#ef5f3c;
  --ink:#0f2a37;
  --text:#3a3a3a;
  --page:#dcdad8;
  --white:#ffffff;
}
*{box-sizing:border-box;margin:0;padding:0}
html,body{width:1200px;height:3272px;overflow:hidden}
body{position:relative;background:var(--page);font-family:'Montserrat',sans-serif;color:var(--text);font-size:13.6px;line-height:20px}
.abs{position:absolute}
.topbar{left:0;top:0;width:1200px;height:36px;background:var(--ink);color:var(--white);font-size:11px;font-weight:600}
.topbar .phone{position:absolute;left:152px;top:9px;display:flex;align-items:center;gap:6px}
.topbar .cta{position:absolute;left:0;width:1200px;top:9px;text-align:center}
.socials{display:flex;gap:5px}
.socials span{width:22px;height:22px;border-radius:50%;background:var(--orange);display:block}
.topbar .socials{position:absolute;left:941px;top:7px}
.header{left:0;top:36px;width:1200px;height:142px;background:var(--teal)}
.brand{display:flex;align-items:center;gap:8px;color:var(--white);font-weight:700;font-size:26px;letter-spacing:1px}
.brand i{width:14px;height:14px;background:#d8b24a;display:block}
.header .brand{position:absolute;left:150px;top:36px}
.search{position:absolute;left:909px;top:40px;width:139px;height:33px;border:2px solid #c8c8c8;border-radius:4px;background:#e9e9e9;font-size:11px;font-weight:600;color:#444;display:flex;align-items:center;justify-content:space-between;padding:0 10px;white-space:nowrap}
.nav{position:absolute;top:114px;left:0;width:1200px;font-size:13px;font-weight:700;color:var(--white);white-space:nowrap}
.nav a{position:absolute;color:inherit;text-decoration:none}
.nav .active{color:var(--orange)}
.nav .muted{color:#9fc9cc}
.caret{display:inline-block;border:6px solid transparent;border-top:7px solid var(--orange);border-bottom:0;margin-left:5px;vertical-align:2px}
.rule{left:0;width:1200px;background:var(--white)}
.hero{left:0;top:184px;width:1200px;height:341px;background:linear-gradient(120deg,#1c3a4a 0%,#2f6f82 40%,#8fb7c4 55%,#1f4c5c 75%,#0f2a37 100%)}
.hero-strip{left:0;top:525px;width:1200px;height:7px;background:var(--teal)}
.hero-box{left:168px;top:239px;width:863px;height:244px;border:2px solid rgba(255,255,255,.5);background:rgba(11,107,115,.55);text-align:center;color:var(--white)}
.hero-box h1{font-size:30px;line-height:43px;font-weight:700;margin-top:16px}
.hero-box p{font-size:25px;line-height:30px;margin-top:22px;font-weight:400}
.btn{display:inline-block;background:var(--orange);color:var(--white);font-weight:700;font-size:13px;padding:0 16px;height:38px;line-height:38px;border-radius:3px;text-decoration:none;white-space:nowrap;text-align:center}
.hero-box .btn{margin-top:22px;min-width:172px;border:2px solid #f7b29f;line-height:34px}
h2{color:var(--teal);font-size:20px;line-height:26px;font-weight:700;white-space:nowrap}
.bar{width:112px;height:4px;background:var(--teal);margin-top:6px}
.ticks{list-style:none}
.ticks li{position:relative;padding-left:30px;margin-bottom:20px}
.ticks li svg{position:absolute;left:4px;top:0}
.mission{left:150px;top:563px;width:435px}
.mission p{margin-top:10px}
.mission p+p{margin-top:20px}
.provide{left:622px;top:561px;width:420px}
.provide .ticks{margin-top:14px}
.card{background:var(--white);top:813px;width:423px;height:430px}
.card .photo{height:218px}
.card .body{padding:20px 22px 0 33px}
.card p{margin-top:26px}
.card .btn{display:block;width:max-content;min-width:169px;margin:30px auto 0}
.band-left{left:150px;top:1312px;width:451px;height:424px;background:var(--teal);color:var(--white);padding:90px 16px 0 43px;font-size:22.5px;line-height:34px;font-weight:700}
.band-right{left:601px;top:1312px;width:449px;height:424px;background:var(--white);padding:38px 20px 0 24px}
.band-right .ticks{margin-top:22px}
.band-right .ticks li{margin-bottom:20px}
.services{left:150px;top:1806px;width:899px;height:314px;background:var(--white);padding:18px 18px 0 19px}
.services p{margin-top:20px}
.res-left{left:150px;top:2188px;width:449px;height:314px;background:var(--white);padding:18px 10px 0 19px}
.res-left p{margin-top:20px}
.res-right{left:599px;top:2188px;width:450px;height:314px;background:var(--teal);color:var(--white);padding:74px 24px 0 52px;font-size:22.5px;line-height:34px;font-weight:700}
.news{left:150px;top:2569px;width:902px;height:286px;border:2px solid var(--teal);background:#e0dedc}
.news h2{text-align:center;margin-top:26px}
.post{position:absolute;top:80px;width:370px}
.post h3{font-size:15px;font-weight:600;color:#333;white-space:nowrap}
.post .date{position:absolute;top:32px;width:79px;height:78px;background:var(--orange);border:2px solid #b9452a;color:var(--white);text-align:center;font-size:18px;line-height:27px;padding-top:10px;font-weight:500}
.post p{position:absolute;top:32px;left:97px;width:262px}
.post p b{color:var(--orange);font-weight:700;white-space:nowrap}
.news .arrow{position:absolute;top:131px}
.news .all{position:absolute;left:0;width:898px;top:236px;text-align:center;color:var(--orange);font-weight:600;font-size:13px}
.footer{left:0;top:2923px;width:1200px;height:303px;background:var(--teal);color:var(--white)}
.fcol{position:absolute;top:50px;width:150px;text-align:center;font-size:12px;line-height:16px}
.fcol h4{font-size:13px;font-weight:700;padding-bottom:6px;border-bottom:3px solid var(--white);width:112px;margin:0 auto 10px}
.fcol ul{list-style:none;text-align:left;display:inline-block;white-space:nowrap}
.fcol li{display:flex;align-items:center;gap:8px}
.fcol li i{width:11px;height:11px;background:var(--orange);display:block}
.footer .socials{justify-content:center}
.footer .socials span{width:16px;height:16px}
.footer .brand{position:absolute;left:0;width:1200px;justify-content:center;top:190px}
.bottombar{left:0;top:3226px;width:1200px;height:46px;background:var(--ink);color:var(--white);font-size:12px;text-align:center;line-height:46px;word-spacing:2px;white-space:nowrap}
</style>
</head>
<body>

<div class="abs topbar">
  <div class="phone">
    <svg width="16" height="16" viewBox="0 0 16 16"><path d="M3 1l3 3-2 2c1 2 3 4 5 5l2-2 3 3-2 3C6 15 1 10 1 3z" fill="#ef5f3c"/></svg>
    800-555-0147
  </div>
  <div class="cta">GET IN TOUCH WITH US TODAY!</div>
  <div class="socials"><span></span><span></span><span></span><span></span></div>
</div>

<div class="abs header">
  <div class="brand"><i></i>HARBORLINE</div>
  <div class="search">SEARCH SITE
    <svg width="18" height="18" viewBox="0 0 18 18"><circle cx="7.5" cy="7.5" r="5.5" fill="none" stroke="#444" stroke-width="1.8"/><path d="M11.5 11.5l5 5" stroke="#444" stroke-width="1.8"/></svg>
  </div>
  <nav class="nav">
    <a class="active" style="left:368px">HOME</a>
    <a style="left:455px">ABOUT</a>
    <a style="left:547px">SOLUTIONS<span class="caret"></span></a>
    <a style="left:672px">RESOURCES<span class="caret"></span></a>
    <a class="muted" style="left:801px">CONTACT</a>
  </nav>
</div>
<div class="abs rule" style="top:178px;height:6px"></div>

<div class="abs hero" role="img" aria-label="Looking up at glass office towers"></div>
<div class="abs hero-strip"></div>
<div class="abs hero-box">
  <h1>Harborline Business Solutions is<br>your trustable security provider.</h1>
  <p>Get in touch with us today!</p>
  <a class="btn">REQUEST A QUOTE</a>
</div>

<section class="abs mission">
  <h2>Our Mission:</h2>
  <p>To provide our customers with comprehensive security, audio/video, and automation with top notch customer service. We Ensure Security with Smart Tools.</p>
  <p>The graded security measures from Harborline Business Solutions ensure the safety of both residential and commercial property. We provide a wide range of Residential and Commercial Security Solutions.</p>
</section>

<section class="abs provide">
  <h2>We provide these Security Solutions:</h2>
  <ul class="ticks">
    <li><svg width="20" height="20" viewBox="0 0 20 20"><circle cx="10" cy="10" r="10" fill="#ef5f3c"/><path d="M5.5 10l3 3 6-6" fill="none" stroke="#fff" stroke-width="2"/></svg>People's safety is our top priority.</li>
    <li><svg width="20" height="20" viewBox="0 0 20 20"><circle cx="10" cy="10" r="10" fill="#ef5f3c"/><path d="M5.5 10l3 3 6-6" fill="none" stroke="#fff" stroke-width="2"/></svg>This includes ensuring that the security system built at your commercial property is configured accurately.</li>
    <li><svg width="20" height="20" viewBox="0 0 20 20"><circle cx="10" cy="10" r="10" fill="#ef5f3c"/><path d="M5.5 10l3 3 6-6" fill="none" stroke="#fff" stroke-width="2"/></svg>Further, it will protect against intruders, burglaries, and holdups.</li>
  </ul>
</section>

<article class="abs card" style="left:150px">
  <div class="photo" role="img" aria-label="Dome security camera mounted on a brick wall" style="background:linear-gradient(135deg,#6d5446,#3b2f2a 50%,#a08878)"></div>
  <div class="body">
    <h2>Commercial Solutions</h2><div class="bar"></div>
    <p>Protect assets and security of your business with Exceptional Commercial Security Installation</p>
    <a class="btn">REQUEST A QUOTE</a>
  </div>
</article>

<article class="abs card" style="left:627px">
  <div class="photo" role="img" aria-label="Smartphone controlling home security devices" style="background:linear-gradient(135deg,#1b2630,#2d5677 55%,#6c9cc0)"></div>
  <div class="body" style="padding:20px 14px 0 27px">
    <h2>Residential Security Solutions</h2><div class="bar"></div>
    <p>Consider a home surveillance device that would do more for you and your family than you ever imagined.</p>
    <a class="btn">REQUEST A QUOTE</a>
  </div>
</article>

<section class="abs band-left">
  We will help secure your company outside of the realm of conventional monitoring technologies. Indeed, we take a customised and comprehensive approach to defence.
  <svg style="display:block;margin:36px 0 0 95px" width="96" height="40" viewBox="0 0 96 40"><path d="M2 20h88M72 4l18 16-18 16" fill="none" stroke="#ef5f3c" stroke-width="4"/></svg>
</section>

<section class="abs band-right">
  <h2>We do this by:</h2>
  <ul class="ticks">
    <li><svg width="20" height="20" viewBox="0 0 20 20"><circle cx="10" cy="10" r="10" fill="#ef5f3c"/><path d="M5.5 10l3 3 6-6" fill="none" stroke="#fff" stroke-width="2"/></svg>Audio &amp; Video Solutions for your commercial property</li>
    <li><svg width="20" height="20" viewBox="0 0 20 20"><circle cx="10" cy="10" r="10" fill="#ef5f3c"/><path d="M5.5 10l3 3 6-6" fill="none" stroke="#fff" stroke-width="2"/></svg>Burglar Alarms &amp; Detectors</li>
    <li><svg width="20" height="20" viewBox="0 0 20 20"><circle cx="10" cy="10" r="10" fill="#ef5f3c"/><path d="M5.5 10l3 3 6-6" fill="none" stroke="#fff" stroke-width="2"/></svg>CCTV cameras equipped with facial recognition technologies enable the technology to identify the offenders.</li>
    <li><svg width="20" height="20" viewBox="0 0 20 20"><circle cx="10" cy="10" r="10" fill="#ef5f3c"/><path d="M5.5 10l3 3 6-6" fill="none" stroke="#fff" stroke-width="2"/></svg>Monitoring of alarms and video recordings 24 hours a day, seven days a week. Addressing all the incidents with an urgent response.</li>
    <li><svg width="20" height="20" viewBox="0 0 20 20"><circle cx="10" cy="10" r="10" fill="#ef5f3c"/><path d="M5.5 10l3 3 6-6" fill="none" stroke="#fff" stroke-width="2"/></svg>Alarm systems and cameras precisely installed so that more of your property is tracked.</li>
  </ul>
</section>

<section class="abs services">
  <h2>Our Commercial Security Services Are Comprensive</h2><div class="bar"></div>
  <p>Flooding, smoke, power outages, temperature fluctuations, and other factors will all be tracked. So, you can take prompt steps before you experience damage.</p>
  <p>But, it all comes down to internal and external security measures. We can combine low-light cameras, smoke and temperature monitoring, noise control, and physical surveillance into a 24/7 commercial security solution. Thus, you can focus on running your business with utmost safety.</p>
  <p>Our commercial security services are comprehensive. In fact, we have worked out how to protect companies from future threats by tailoring our strategy to each new customer. Therefore, whatever business you are into, we provide you with a security solution that physically protects you, your employees, clients, and property.</p>
</section>

<section class="abs res-left">
  <h2>Our Residential Security Solutions</h2><div class="bar"></div>
  <p>Harborline Business Solutions is your trustable security provider. Also, as certified professionals carry out the installation, you have everything under control. Your home is being securely watched from various points, with cameras capable of tracking any intruder's path.</p>
  <p>Specifically, we offer Residential Intrusion Detection Security Systems, Residential Alarm, Residential Network Wi-Fi, CCTVs and residential home automation.</p>
</section>
<section class="abs res-right">
  Consider a home surveillance device that would do more for you and your family than you ever imagined.
  <svg style="display:block;margin:30px 0 0 125px" width="96" height="40" viewBox="0 0 96 40"><path d="M94 20H6M24 4L6 20l18 16" fill="none" stroke="#ef5f3c" stroke-width="4"/></svg>
</section>

<section class="abs news">
  <h2>Harborline Latest News</h2>
  <svg class="arrow" style="left:23px" width="28" height="28" viewBox="0 0 28 28"><circle cx="14" cy="14" r="12.5" fill="none" stroke="#ef5f3c" stroke-width="2"/><path d="M21 14H8M13 9l-5 5 5 5" fill="none" stroke="#ef5f3c" stroke-width="2"/></svg>
  <div class="post" style="left:79px">
    <h3>Why Which Camera You Choose Matters</h3>
    <div class="date">21<br>FEB</div>
    <p>Lorem ipsum dolor sit amet, consectetur adipiscing elit. Integer sit amet sem imperdiet, tincidunt dolor eu. <b>READ MORE</b></p>
  </div>
  <div class="post" style="left:487px">
    <h3>Wireless Video Capture for Better Security</h3>
    <div class="date" style="left:4px">10<br>SEP</div>
    <p style="left:101px">Lorem ipsum dolor sit amet, consectetur adipiscing elit. Integer sit amet sem imperdiet, tincidunt dolor eu. <b>READ MORE</b></p>
  </div>
  <svg class="arrow" style="left:851px" width="28" height="28" viewBox="0 0 28 28"><circle cx="14" cy="14" r="12.5" fill="none" stroke="#ef5f3c" stroke-width="2"/><path d="M7 14h13M15 9l5 5-5 5" fill="none" stroke="#ef5f3c" stroke-width="2"/></svg>
  <div class="all">Read All Posts</div>
</section>

<div class="abs rule" style="top:2915px;height:8px"></div>
<footer class="abs footer">
  <div class="fcol" style="left:179px"><h4>About</h4><div class="socials"><span></span><span></span><span></span><span></span></div></div>
  <div class="fcol" style="left:391px"><h4>Solutions</h4><ul><li><i></i>Commercial</li><li><i></i>Residential</li></ul></div>
  <div class="fcol" style="left:621px"><h4>Resources</h4><ul><li><i></i>Packages</li><li><i></i>Specials</li></ul></div>
  <div class="fcol" style="left:821px;width:220px"><h4>Contact</h4><ul><li><i></i>info@harborline-example.com</li><li><i></i>800-555-0147</li></ul></div>
  <div class="brand"><i></i>HARBORLINE</div>
</footer>
<div class="abs bottombar">Copyright 2021. &nbsp;&nbsp;&nbsp; | &nbsp;&nbsp;&nbsp; Harborline Business Solutions &nbsp;&nbsp;&nbsp; | &nbsp;&nbsp;&nbsp; All Rights Reserved.</div>

</body>
</html>
```